Business Card Design

We need a business card design for a new company called Riverbend Advisory, LLC. We are a project management and software engineering consulting company. We prefer to use blues but am open to any colors. We would like out design to show strength and creativity.

I've uploaded new logo designs to the project.  Please use these logo designs for the business card. Thanks!

Industry/Entity Type

Software

Contact Information for Business Card

Daniel Whitford
Consultant
Owner

Riverbend Advisory, LLC

2716 5th St. S #4372
Arlington, VA 22198

703-555-0187
dwhitford@rvbadv.example
www.rvbadv.example

```html
<!DOCTYPE html>
<html lang="en">
<head>
<meta charset="utf-8">
<title>Riverbend Advisory, LLC – Business Card</title>
<link rel="stylesheet" href="https://fonts.googleapis.com/css2?family=Exo+2:wght@400;500;600;700&display=swap">
<style>
  :root {
    --backdrop: #d9dadb;
    --navy: #0f3a5c;
    --navy-deep: #0b2c48;
    --navy-light: #24506f;
    --band-grey: #e4e6e8;
    --white: #ffffff;
    --ink-navy: #143e62;
    --text-light: #e9eef3;
  }
  * { box-sizing: border-box; margin: 0; padding: 0; }
  html, body {
    width: 1200px; height: 910px; overflow: hidden;
    background: var(--backdrop);
    font-family: "Exo 2", "Segoe UI", sans-serif;
  }
  .canvas { position: relative; width: 1200px; height: 910px; }
  .card {
    position: absolute; left: 240px; width: 720px; height: 410px;
    border-radius: 22px; overflow: hidden;
    box-shadow: 0 10px 26px rgba(0,0,0,0.18);
  }

  /* Front */
  .card-front {
    top: 30px;
    background: linear-gradient(135deg, var(--navy-light) 0%, var(--navy) 45%, var(--navy-deep) 100%);
    display: flex; flex-direction: column; align-items: center; justify-content: center;
    color: var(--white);
  }
  .brand-name {
    font-weight: 600; letter-spacing: 3px; text-transform: uppercase;
    display: flex; align-items: center; gap: 14px; white-space: nowrap;
  }
  .brand-mark { width: 26px; height: 26px; background: currentColor; flex: none; }
  .card-front .brand-name { font-size: 40px; color: var(--white); }
  .front-website { margin-top: 26px; font-size: 20px; font-weight: 500; letter-spacing: 2px; }

  /* Back */
  .card-back { top: 470px; background: var(--band-grey); }
  .back-panel {
    position: absolute; left: 0; right: 0; top: 120px; bottom: 0;
    background: radial-gradient(ellipse at 45% 40%, var(--navy-light) 0%, var(--navy) 55%, var(--navy-deep) 100%);
  }
  .logo-plate {
    position: absolute; left: 400px; top: 50px; width: 290px; height: 104px;
    background: var(--white);
    display: flex; align-items: center; justify-content: center;
  }
  .logo-plate .brand-name { font-size: 20px; color: var(--ink-navy); gap: 10px; letter-spacing: 2px; }
  .logo-plate .brand-mark { width: 16px; height: 16px; }

  .holder {
    position: absolute; left: 60px; top: 134px; color: var(--text-light);
    display: flex; flex-direction: column; gap: 4px;
  }
  .holder-name { font-size: 22px; font-weight: 500; letter-spacing: 2px; text-transform: uppercase; }
  .holder-title { font-size: 13px; letter-spacing: 1.5px; text-transform: uppercase; padding-left: 2px; }

  .contact-list {
    position: absolute; list-style: none; color: var(--text-light);
    font-size: 18px; letter-spacing: 1px;
  }
  .contact-list li { display: flex; align-items: center; gap: 14px; margin-bottom: 18px; }
  .contact-list .multi { align-items: flex-start; line-height: 1.25; }
  .contact-primary { left: 42px; top: 212px; }
  .contact-secondary { left: 420px; top: 290px; font-size: 16px; }
  .icon { width: 26px; height: 26px; flex: none; }
</style>
</head>
<body>
<main class="canvas">

  <section class="card card-front" aria-label="Business card front">
    <div class="brand-name"><span class="brand-mark"></span>Riverbend Advisory</div>
    <p class="front-website">www.rvbadv.example</p>
  </section>

  <section class="card card-back" aria-label="Business card back">
    <div class="back-panel"></div>
    <div class="logo-plate">
      <div class="brand-name"><span class="brand-mark"></span>Riverbend Advisory</div>
    </div>

    <div class="holder">
      <span class="holder-name">Daniel Whitford</span>
      <span class="holder-title">Consultant / Owner</span>
    </div>

    <ul class="contact-list contact-primary">
      <li>
        <svg class="icon" viewBox="0 0 26 26" aria-hidden="true"><circle cx="13" cy="13" r="11.5" fill="none" stroke="#e9eef3" stroke-width="1.6"/><path d="M9.5 7.5c-1 .6-1.6 1.6-1.2 3 .9 3 3.3 5.6 6.3 6.7 1.3.5 2.4 0 3-1l-2-2-1.5.8c-1.3-.6-2.4-1.8-3-3.1l.9-1.4z" fill="#e9eef3"/></svg>
        703-555-0187
      </li>
      <li>
        <svg class="icon" viewBox="0 0 26 26" aria-hidden="true"><circle cx="13" cy="13" r="11.5" fill="none" stroke="#e9eef3" stroke-width="1.6"/><rect x="7.5" y="9" width="11" height="8" fill="none" stroke="#e9eef3" stroke-width="1.4"/><path d="M7.5 9l5.5 4.5L18.5 9" fill="none" stroke="#e9eef3" stroke-width="1.4"/></svg>
        dwhitford@rvbadv.example
      </li>
    </ul>

    <ul class="contact-list contact-secondary">
      <li class="multi">
        <svg class="icon" viewBox="0 0 26 26" aria-hidden="true"><circle cx="13" cy="13" r="11.5" fill="none" stroke="#e9eef3" stroke-width="1.6"/><path d="M13 6.5a4.2 4.2 0 0 0-4.2 4.2c0 3.2 4.2 8.3 4.2 8.3s4.2-5.1 4.2-8.3A4.2 4.2 0 0 0 13 6.5z" fill="none" stroke="#e9eef3" stroke-width="1.4"/><circle cx="13" cy="10.7" r="1.5" fill="#e9eef3"/></svg>
        <span>2716 5th St. S #4372<br>Arlington, VA 22198</span>
      </li>
      <li>
        <svg class="icon" viewBox="0 0 26 26" aria-hidden="true"><circle cx="13" cy="13" r="11.5" fill="none" stroke="#e9eef3" stroke-width="1.6"/><circle cx="13" cy="13" r="6" fill="none" stroke="#e9eef3" stroke-width="1.3"/><ellipse cx="13" cy="13" rx="2.6" ry="6" fill="none" stroke="#e9eef3" stroke-width="1.2"/><path d="M7 13h12" stroke="#e9eef3" stroke-width="1.2"/></svg>
        www.rvbadv.example
      </li>
    </ul>
  </section>

</main>
</body>
</html>
```